Olive Oil label for bottle 0.5l approx. 10x12 cm

I am running a Spa hotel in Bavaria (logo attached) and my family lives in Greece (Bavarian and Greek flag have the same colors). They produce organic olive oil first cold pressed extra virgin. I would need a label for 0,5 liter bottles to reach them out to my guests and they should see the high quality of the olive oil and the family connection Spa-hotel Bavaria to family in Greece. The name of the family is Merovski, the hotel is called Talgrund, the olive oil comes from Greece/Argolis/Kranidi. The name of the small olive company is Dorin Herons. There should be a space for the best before date and the organic control number (handwritten) . The hotel logo is not mandatory. Should look nice 😉

```html
<!DOCTYPE html>
<html lang="en">
<head>
<meta charset="utf-8">
<title>Merovski Extra Virgin Olive Oil – Label</title>
<link rel="stylesheet" href="https://fonts.googleapis.com/css2?family=Tinos:wght@400&family=Kaushan+Script&display=swap">
<style>
  :root {
    --page-bg: #f4f4f2;
    --label-dark: #2b2c2c;
    --label-mid: #3a3b3b;
    --gold-light: #efe2a2;
    --gold: #c9a548;
    --gold-deep: #9a6a26;
    --silver: #d9d9d6;
    --sage: #7f948e;
    --olive-light: #b9c24a;
    --olive-dark: #5c6b1e;
    --leaf-tone: #4a5350;
  }
  * { box-sizing: border-box; margin: 0; padding: 0; }
  html, body { width: 1200px; height: 1200px; overflow: hidden; }
  body {
    background: var(--page-bg);
    font-family: "Tinos", "Times New Roman", serif;
    position: relative;
  }
  .label {
    position: absolute;
    left: 389px;
    top: 50px;
    width: 422px;
    height: 1100px;
    background: radial-gradient(ellipse at 50% 55%, var(--label-mid) 0%, var(--label-dark) 75%);
    color: var(--silver);
    box-shadow: 0 6px 24px rgba(0,0,0,.18);
  }
  .label > * { position: absolute; left: 0; right: 0; text-align: center; }
  .leaf-border {
    top: 0; height: 112px;
    background: linear-gradient(180deg, #333535 0%, var(--leaf-tone) 45%, #2f3030 100%);
    opacity: .75;
  }
  .hotel-name {
    top: 150px;
    font-size: 44px;
    line-height: 50px;
    color: var(--sage);
    letter-spacing: 1px;
  }
  .hotel-name .dot {
    display: inline-block;
    width: 10px; height: 10px;
    border-radius: 50%;
    background: var(--sage);
    vertical-align: middle;
    margin-left: 8px;
  }
  .family-name {
    top: 266px;
    font-family: "Kaushan Script", cursive;
    font-size: 46px;
    line-height: 56px;
    color: var(--gold);
  }
  .olive-art {
    top: 360px;
    left: 92px; right: auto;
    width: 238px; height: 150px;
    border-radius: 50%;
    background: radial-gradient(ellipse at 45% 55%, var(--olive-light) 0%, var(--olive-dark) 70%, rgba(92,107,30,0) 100%);
  }
  .grade {
    top: 548px;
    left: 110px; right: auto;
    font-size: 24px;
    line-height: 28px;
    letter-spacing: 1.5px;
    color: var(--silver);
  }
  .rule {
    height: 1px;
    background: linear-gradient(90deg, rgba(201,165,72,0), var(--gold) 30%, var(--gold) 70%, rgba(201,165,72,0));
  }
  .rule-top { top: 584px; left: 96px; right: 56px; }
  .product {
    top: 588px;
    right: 62px; left: auto;
    text-align: right;
    font-size: 86px;
    line-height: 80px;
    background: linear-gradient(90deg, var(--gold-light) 0%, var(--gold) 50%, var(--gold-deep) 100%);
    -webkit-background-clip: text;
    background-clip: text;
    color: transparent;
  }
  .organic-badge {
    top: 754px;
    left: 62px; right: auto;
    width: 90px; height: 90px;
    border-radius: 50%;
    border: 2px solid var(--gold);
    box-shadow: inset 0 0 0 8px var(--label-dark), inset 0 0 0 9px var(--gold);
  }
  .branch-art {
    top: 800px;
    left: 150px; right: auto;
    width: 130px; height: 84px;
    background: radial-gradient(ellipse at 50% 50%, rgba(201,165,72,.55) 0%, rgba(154,106,38,.25) 60%, rgba(154,106,38,0) 100%);
    border-radius: 50%;
  }
  .producer {
    top: 912px;
    font-size: 27px;
    line-height: 32px;
    letter-spacing: 1px;
    color: var(--silver);
  }
  .origin {
    top: 958px;
    font-size: 21px;
    line-height: 26px;
    color: var(--silver);
  }
  .rule-bottom { top: 990px; left: 80px; right: 80px; }
  .volume {
    top: 996px;
    font-size: 24px;
    line-height: 28px;
    color: var(--gold);
  }
  .volume small { font-size: 12px; color: var(--silver); }
  .write-in {
    top: 1038px;
    left: 56px; right: 56px;
    display: flex;
    gap: 22px;
    font-size: 13px;
    line-height: 16px;
    color: var(--silver);
  }
  .write-in .field {
    flex: 1;
    display: flex;
    align-items: flex-end;
    gap: 6px;
    white-space: nowrap;
  }
  .write-in .blank {
    flex: 1;
    height: 22px;
    border-bottom: 1px dotted var(--gold);
  }
</style>
</head>
<body>
  <section class="label">
    <div class="leaf-border" role="img" aria-label="Engraved olive leaves and branches pattern"></div>
    <div class="hotel-name">Talgrund<span class="dot"></span></div>
    <div class="family-name">Merovski</div>
    <div class="olive-art" role="img" aria-label="Illustration of green olives on a branch with leaves"></div>
    <div class="grade">EXTRA VIRGIN</div>
    <div class="rule rule-top"></div>
    <div class="product">OLIVE<br>OIL</div>
    <div class="organic-badge"></div>
    <div class="branch-art" role="img" aria-label="Gold olive branch ornament"></div>
    <div class="producer">DORIN HERONS</div>
    <div class="origin">Greece/Argolis/Kranidi</div>
    <div class="rule rule-bottom"></div>
    <div class="volume"><small>Net W.</small> 500 ml ℮</div>
    <div class="write-in">
      <div class="field"><span>Best before:</span><span class="blank"></span></div>
      <div class="field"><span>Organic control no.:</span><span class="blank"></span></div>
    </div>
  </section>
</body>
</html>
```